INNOVATIVE DESIGN NEEDED FOR FINANCIAL COMPANY

INTERNATIONAL FIRM IN HONG KONG NEEDS A MODERN BUSINESS CARD DESIGN. ONE SIDE ENGLISH OTHER SIDE IN CHINESE. WE ARE OPEN TO CHANGING FONTS AND COLOR. SHOULD BE A CARD THAT IS PROFESSIONAL DEALING WITH HIGH NET WORTH CLIENTELE. BOTH SIDES OF THE CARD WILL BE THE SAME, HOWEVER, THE WORDING ON ONE SIDE WILL BE ENGLISH AND THE OTHER SIDE IN CHINESE (CAN ASSIST IN THE LETTERING - CAN PROVIDE ONCE CARD DESIGN IS ACCEPTED.

Target Market(s)

Hong Kong/CHINA

Contact Information for Business Card

ATTRACTIVE MODERN

```html
<!DOCTYPE html>
<html lang="en">
<head>
<meta charset="utf-8">
<title>Linden Crest Asset Management – Business Cards</title>
<link rel="stylesheet" href="https://fonts.googleapis.com/css2?family=Oswald:wght@600&family=Roboto:wght@400;900&family=Noto+Sans+SC:wght@300;400&family=Noto+Sans+TC:wght@900&display=swap">
<style>
  :root {
    --bg: #1d1d1e;
    --paper: #ffffff;
    --slate: #3c3c3e;
    --green: #148c68;
    --ink: #3a3a3a;
    --muted: #6b6b6b;
  }
  * { box-sizing: border-box; margin: 0; padding: 0; }
  html, body { width: 1200px; height: 895px; overflow: hidden; background: var(--bg); }
  .stage {
    width: 1200px; height: 895px;
    display: flex; flex-direction: column; align-items: center; justify-content: center; gap: 40px;
  }
  .card {
    position: relative; width: 680px; height: 388px;
    background: var(--paper); overflow: hidden;
    box-shadow: 0 14px 30px rgba(0,0,0,.55);
    font-family: "Roboto", sans-serif;
  }
  .card-art { position: absolute; inset: 0; }
  .brand { position: absolute; left: 42px; top: 40px; color: var(--ink); }
  .brand-zh { font-family: "Noto Sans TC", sans-serif; font-weight: 900; font-size: 31px; letter-spacing: 2px; line-height: 1.1; }
  .brand-en { font-family: "Roboto", sans-serif; font-weight: 900; font-size: 12.5px; letter-spacing: 2.2px; color: var(--muted); margin-top: 2px; }
  .person { position: absolute; left: 60px; top: 118px; }
  .person-name { color: var(--green); line-height: 1.1; }
  .person-name.en { font-family: "Oswald", sans-serif; font-weight: 600; font-size: 28px; }
  .person-name.zh { font-family: "Noto Sans SC", sans-serif; font-weight: 300; font-size: 28px; letter-spacing: 2px; }
  .person-role { font-size: 16px; color: var(--ink); margin-top: 2px; }
  .person-role.zh { font-family: "Noto Sans SC", sans-serif; font-size: 15px; }
  .contacts { position: absolute; left: 60px; top: 200px; list-style: none; }
  .contacts li { display: flex; align-items: center; gap: 9px; font-size: 15.5px; color: var(--ink); line-height: 23px; }
  .contacts svg { width: 13px; height: 13px; fill: var(--green); flex: none; }
  .address { position: absolute; right: 30px; bottom: 24px; color: #fff; font-size: 15.5px; letter-spacing: .3px; }
</style>
</head>
<body>
<main class="stage">

  <section class="card card-zh" lang="zh">
    <svg class="card-art" viewBox="0 0 680 388" aria-hidden="true">
      <path d="M0,362 Q535,354 664,-5 L680,-5 L680,388 L0,388 Z" fill="var(--slate)"/>
      <path d="M-10,358 Q530,350 656,-10" fill="none" stroke="var(--paper)" stroke-width="8"/>
      <path d="M-10,348 Q515,338 638,-10" fill="none" stroke="var(--green)" stroke-width="11"/>
      <circle cx="592" cy="96" r="78" fill="var(--green)" stroke="var(--paper)" stroke-width="6"/>
    </svg>
    <header class="brand">
      <div class="brand-zh">林峰資產管理有限公司</div>
      <div class="brand-en">Linden Crest Asset Management Ltd</div>
    </header>
    <div class="person">
      <div class="person-name zh">马库斯·里德</div>
      <div class="person-role zh">管理伙伴</div>
    </div>
    <ul class="contacts">
      <li><svg viewBox="0 0 16 16"><path d="M3 1l3 3-2 2c1 2 3 4 5 5l2-2 3 3-2 3C6 15 1 10 0 4z"/></svg>000 000 0000</li>
      <li><svg viewBox="0 0 16 16"><path d="M0 3h16v10H0zM1 4l7 5 7-5v-1H1z"/></svg>m_reed@lindencrestmgmt.com</li>
      <li><svg viewBox="0 0 16 16"><circle cx="8" cy="8" r="7.5"/><path d="M.5 8h15M8 .5v15" stroke="#fff" stroke-width="1"/></svg>www.lindencrestmgmt.com</li>
    </ul>
    <p class="address">2140 rue Beaumont, Ville Saint-Claire, QC H3K 2W8</p>
  </section>

  <section class="card card-en">
    <svg class="card-art" viewBox="0 0 680 388" aria-hidden="true">
      <path d="M0,362 Q535,354 664,-5 L680,-5 L680,388 L0,388 Z" fill="var(--slate)"/>
      <path d="M-10,358 Q530,350 656,-10" fill="none" stroke="var(--paper)" stroke-width="8"/>
      <path d="M-10,348 Q515,338 638,-10" fill="none" stroke="var(--green)" stroke-width="11"/>
      <circle cx="592" cy="96" r="78" fill="var(--green)" stroke="var(--paper)" stroke-width="6"/>
    </svg>
    <header class="brand">
      <div class="brand-zh" lang="zh">林峰資產管理有限公司</div>
      <div class="brand-en">Linden Crest Asset Management Ltd</div>
    </header>
    <div class="person">
      <div class="person-name en">Marcus Reed</div>
      <div class="person-role">Managing Partner</div>
    </div>
    <ul class="contacts">
      <li><svg viewBox="0 0 16 16"><path d="M3 1l3 3-2 2c1 2 3 4 5 5l2-2 3 3-2 3C6 15 1 10 0 4z"/></svg>000 000 0000</li>
      <li><svg viewBox="0 0 16 16"><path d="M0 3h16v10H0zM1 4l7 5 7-5v-1H1z"/></svg>m_reed@lindencrestmgmt.com</li>
      <li><svg viewBox="0 0 16 16"><circle cx="8" cy="8" r="7.5"/><path d="M.5 8h15M8 .5v15" stroke="#fff" stroke-width="1"/></svg>www.lindencrestmgmt.com</li>
    </ul>
    <p class="address">2140 rue Beaumont, Ville Saint-Claire, QC H3K 2W8</p>
  </section>

</main>
</body>
</html>
```